Clean Stationary Design For Print Shop

I need a clean stationary set that properly represents a local print and copy shop to make it look amazing. It should do the following:
- Compliment the color scheme of the logo.
- Be clean and sharp.
- Be colorful but but balanced.

This is what I need designed:
- Business Card
- Letter Head
- Envelop

Target Market(s)

Local customers and businesses, including hospitals and schools.

Industry/Entity Type

Digital Printing

Requirements
Must have
• Clean business card with logo on front and full color back with faded logo on it and social icons with @tollworthmarks beside each one (Pagelark & Glimmora).

```html
<!DOCTYPE html>
<html lang="en">
<head>
<meta charset="utf-8">
<title>Tollworth Marks — Business Card</title>
<link href="https://fonts.googleapis.com/css2?family=Mulish:wght@400;600;700&display=swap" rel="stylesheet">
<style>
  :root {
    --backdrop: #767676;
    --paper: #ffffff;
    --ink: #111111;
    --text: #3a3a3a;
    --accent: #ff2d4b;
    --dark: #232323;
    --dark-pattern: #1c1c1c;
  }
  html, body {
    margin: 0;
    padding: 0;
    width: 1200px;
    height: 1200px;
    overflow: hidden;
    background: var(--backdrop);
    font-family: "Mulish", Arial, sans-serif;
  }
  .canvas { position: relative; width: 1200px; height: 1200px; }

  .card {
    position: absolute;
    left: 262px;
    width: 686px;
    height: 392px;
    overflow: hidden;
    box-shadow: 0 14px 24px rgba(0,0,0,0.28);
  }
  .card-front { top: 165px; background: var(--paper); }
  .card-back { top: 653px; background: var(--dark); }

  .brand {
    position: absolute;
    left: 67px;
    top: 172px;
    display: flex;
    align-items: flex-start;
    gap: 10px;
  }
  .brand-square {
    width: 36px;
    height: 36px;
    background: var(--accent);
    margin-top: 4px;
  }
  .brand-name {
    font-size: 29px;
    font-weight: 600;
    color: var(--ink);
    line-height: 1;
    letter-spacing: -0.5px;
  }
  .brand-tagline {
    margin-top: 4px;
    font-size: 10.5px;
    font-weight: 700;
    color: #666;
    letter-spacing: 0.2px;
  }

  .divider {
    position: absolute;
    left: 369px;
    top: 90px;
    width: 2px;
    height: 193px;
    background: #555;
  }

  .contact {
    position: absolute;
    left: 399px;
    top: 90px;
    color: var(--text);
  }
  .contact-name {
    margin: 0;
    font-size: 22px;
    font-weight: 600;
    color: var(--accent);
    line-height: 1.1;
  }
  .contact-role {
    margin: 4px 0 0;
    font-size: 15px;
    color: var(--ink);
  }
  .contact-address {
    margin: 16px 0 0;
    font-size: 15px;
    line-height: 19px;
    font-style: normal;
  }
  .contact-lines {
    list-style: none;
    margin: 14px 0 0;
    padding: 0;
    font-size: 15px;
    line-height: 19.5px;
  }
  .contact-lines li { display: flex; align-items: center; gap: 9px; }
  .contact-lines svg { width: 14px; height: 14px; fill: var(--accent); flex: none; }

  .web-band {
    position: absolute;
    left: 0;
    top: 333px;
    width: 524px;
    height: 30px;
    background: var(--accent);
    color: #fff;
    font-size: 16px;
    letter-spacing: 8.6px;
    line-height: 30px;
    padding-left: 81px;
    box-sizing: border-box;
    white-space: nowrap;
  }
  .dark-band {
    position: absolute;
    left: 533px;
    top: 333px;
    width: 153px;
    height: 30px;
    background: var(--dark);
  }
  .band-square {
    position: absolute;
    left: 533px;
    top: 334px;
    width: 18px;
    height: 18px;
    background: #fff;
  }

  .back-pattern {
    position: absolute;
    inset: 0;
    background:
      linear-gradient(180deg,
        var(--dark-pattern) 0%, var(--dark) 12%,
        var(--dark-pattern) 25%, var(--dark) 37%,
        var(--dark-pattern) 50%, var(--dark) 62%,
        var(--dark-pattern) 75%, var(--dark) 87%,
        var(--dark-pattern) 100%);
  }
  .back-brand {
    position: absolute;
    right: 40px;
    top: 302px;
    display: flex;
    align-items: center;
    gap: 10px;
  }
  .back-square { width: 30px; height: 30px; background: var(--accent); }
  .back-name {
    font-size: 28px;
    font-weight: 600;
    color: var(--accent);
    letter-spacing: -0.5px;
  }
</style>
</head>
<body>
<main class="canvas">
  <section class="card card-front">
    <div class="brand">
      <div class="brand-square"></div>
      <div>
        <div class="brand-name">Tollworth Marks</div>
        <div class="brand-tagline">BETTER QUALITY, SPEED &amp; PRICES</div>
      </div>
    </div>

    <div class="divider"></div>

    <div class="contact">
      <h1 class="contact-name">Dorian Vale</h1>
      <p class="contact-role">President</p>
      <address class="contact-address">4120 Fernwick Road<br>Brackley, Oregon 97231</address>
      <ul class="contact-lines">
        <li>
          <svg viewBox="0 0 16 16"><path d="M3.6 1.2l2.2 2.6c.3.4.3.9 0 1.3L4.7 6.3c.8 1.9 2.3 3.4 4.2 4.3l1.2-1.1c.4-.3.9-.3 1.3 0l2.6 2.1c.4.3.4.9.1 1.3l-1.2 1.5c-.4.5-1 .7-1.6.5C6.1 13.5 2.6 10 1.3 4.6c-.2-.6 0-1.2.5-1.6l1.3-1.9c.1-.1.3 0 .5.1z"/></svg>
          <span>555-214-7730</span>
        </li>
        <li>
          <svg viewBox="0 0 16 16"><path d="M4.5 0h7c.8 0 1.5.7 1.5 1.5v13c0 .8-.7 1.5-1.5 1.5h-7C3.7 16 3 15.3 3 14.5v-13C3 .7 3.7 0 4.5 0zm.5 2v11h6V2H5zm3 11.6a.9.9 0 100 1.8.9.9 0 000-1.8z"/></svg>
          <span>555-608-1942</span>
        </li>
        <li>
          <svg viewBox="0 0 16 16"><path d="M4 1h6l2 2v3H4V1zM1 7h14v6h-2v-2H3v2H1V7zm3 5h8v3H4v-3z"/></svg>
          <span>555-391-2276</span>
        </li>
        <li>
          <svg viewBox="0 0 16 16"><path d="M1 3h14v10H1V3zm1.5 1.5v.3L8 8.8l5.5-4v-.3h-11zm0 2.2v4.8h11V6.7L8 10.6 2.5 6.7z"/></svg>
          <span>info@tollworthmarks.com</span>
        </li>
      </ul>
    </div>

    <div class="web-band">www.TollworthMarks.com</div>
    <div class="dark-band"></div>
    <div class="band-square"></div>
  </section>

  <section class="card card-back">
    <div class="back-pattern" role="img" aria-label="Faint repeating brand-mark pattern in dark charcoal tones"></div>
    <div class="back-brand">
      <div class="back-square"></div>
      <div class="back-name">Tollworth Marks</div>
    </div>
  </section>
</main>
</body>
</html>
```